TrunvaX Calendar 2020 - Just need fine tuning

All design and content are ready. Just require some fine tuning
The date needs to be changed to 2020
and the address should be changed. I will provide new addresses.
Everything else can stay the same.

Other font styles liked:
• see file

Colors
a64599

```html
<!DOCTYPE html>
<html lang="en">
<head>
<meta charset="UTF-8">
<title>Personal Information</title>
<link rel="stylesheet" href="https://fonts.googleapis.com/css2?family=Dancing+Script:wght@700&family=Source+Sans+3:wght@400&display=swap">
<style>
  :root {
    --purple: #a64599;
    --label: #6d6e70;
    --rule: #a7a9ac;
    --paper: #ffffff;
  }
  * { box-sizing: border-box; margin: 0; padding: 0; }
  html, body { width: 715px; height: 1200px; overflow: hidden; background: var(--paper); }
  .page {
    position: relative;
    width: 715px;
    height: 1200px;
    font-family: "Source Sans 3", Arial, sans-serif;
    color: var(--label);
  }
  .page-title {
    position: absolute;
    left: 95px;
    top: 52px;
    color: var(--purple);
    white-space: nowrap;
  }
  .page-title .script {
    font-family: "Dancing Script", cursive;
    font-weight: 700;
    font-size: 68px;
    letter-spacing: 0.5px;
  }
  .page-title .plain {
    font-size: 33px;
    margin-left: 8px;
  }
  .field {
    position: absolute;
    left: 97px;
    width: 550px;
    display: flex;
    align-items: flex-end;
    font-size: 21px;
    line-height: 1;
  }
  .field .label { white-space: nowrap; padding-right: 8px; }
  .field .fill { flex: 1; border-bottom: 1.5px solid var(--rule); height: 1px; }
  .rule {
    position: absolute;
    left: 97px;
    width: 550px;
    border-bottom: 1.5px solid var(--rule);
  }
</style>
</head>
<body>
<main class="page">
  <h1 class="page-title"><span class="script">Personal</span><span class="plain">Information</span></h1>

  <div class="field" style="top:160px"><span class="label">Name:</span><span class="fill"></span></div>
  <div class="field" style="top:203px"><span class="label">Mask&nbsp; Model:</span><span class="fill"></span></div>
  <div class="field" style="top:247px"><span class="label">Device&nbsp; Model:</span><span class="fill"></span></div>
  <div class="field" style="top:289px"><span class="label">Tubing Type:</span><span class="fill"></span></div>
  <div class="field" style="top:333px"><span class="label">Date Purchased:</span><span class="fill"></span></div>

  <div class="field" style="top:425px"><span class="label">Next Follow-up Appointment:</span><span class="fill"></span></div>
  <div class="rule" style="top:485px"></div>
  <div class="rule" style="top:524px"></div>

  <div class="field" style="top:575px"><span class="label">Next Follow-up Appointment:</span><span class="fill"></span></div>
  <div class="rule" style="top:635px"></div>
  <div class="rule" style="top:674px"></div>

  <div class="field" style="top:724px"><span class="label">Next Follow-up Appointment:</span><span class="fill"></span></div>
  <div class="rule" style="top:784px"></div>
  <div class="rule" style="top:823px"></div>

  <div class="field" style="top:876px"><span class="label">Next Follow-up Appointment:</span><span class="fill"></span></div>
  <div class="rule" style="top:936px"></div>
  <div class="rule" style="top:975px"></div>

  <div class="field" style="top:1025px"><span class="label">Next Follow-up Appointment:</span><span class="fill"></span></div>
  <div class="rule" style="top:1085px"></div>
  <div class="rule" style="top:1124px"></div>
</main>
</body>
</html>
```